Showroom Quote Web Application - Material Design wanted

This web app is an internal application that will be used by one of our customers to build quotes and produce orders of retail items with their customers

the overall design should use the colour pallet provided and have a clean and simple interface

we'd like to go with a material design type of look

attached mockups are just a rough stab at some layouts to give you an example, please feel free to reach out with any questions.

Please don't get hung up on the specific pages, they were intended to provide context, we are looking for a high level design using the provided colour schemes and fonts, additional work may follow for the selected designer when it comes to specific pages or work flows.

Sorry for the short timeline, we have a tight deadline on this one.

Target Market(s)

internal application for customer

Industry/Entity Type

Retail

Other font styles liked:
• see attached doc for fonts

Requirements
Must have
• simple and clean interface
• intuitive design
Nice to have
• see attached documents for logo colour schemes and fonts
• these must be incorporated into the design

```html
<!DOCTYPE html>
<html lang="en">
<head>
<meta charset="utf-8">
<title>Showroom Quote – Staff View</title>
<link href="https://fonts.googleapis.com/css2?family=Roboto:wght@400;500;700&display=swap" rel="stylesheet">
<style>
  :root {
    --navy: #03296a;
    --navy-field: #2c4c84;
    --navy-search: #3e5a8f;
    --gold: #b38f4f;
    --page: #f5f5f5;
    --white: #ffffff;
    --ink: #222;
    --ink-soft: #555;
    --ink-muted: #888;
    --row-alt: #f6f6f6;
    --line: #e3e3e3;
  }
  * { box-sizing: border-box; margin: 0; padding: 0; }
  html, body { width: 1200px; height: 1200px; overflow: hidden; }
  body { background: var(--page); font-family: 'Roboto', sans-serif; color: var(--ink); position: relative; }

  .screen { position: absolute; left: 157px; width: 886px; background: var(--page); box-shadow: 0 1px 6px rgba(0,0,0,.08); overflow: hidden; }
  .screen--quote { top: 30px; height: 556px; }
  .screen--item { top: 610px; height: 555px; }

  .appbar { position: absolute; left: 0; top: 0; width: 100%; height: 40px; background: var(--white); display: flex; align-items: center; padding: 0 18px; }
  .appbar__menu { width: 13px; height: 9px; border-top: 1.5px solid #777; border-bottom: 1.5px solid #777; position: relative; margin-right: 14px; }
  .appbar__menu::after { content: ""; position: absolute; left: 0; right: 0; top: 2.5px; border-top: 1.5px solid #777; }
  .appbar__brand { font-weight: 700; font-size: 12.5px; color: #555; letter-spacing: .3px; }
  .appbar__user { margin-left: auto; font-size: 8px; color: var(--ink-muted); }
  .appbar__avatar { width: 22px; height: 22px; border-radius: 50%; background: linear-gradient(160deg, #c9d5e4, #4f6f96 55%, #22344f); margin-left: 20px; }
  .appbar__more { width: 3px; height: 11px; margin-left: 10px; background: radial-gradient(circle, #777 1.2px, transparent 1.4px) 0 0/3px 4px repeat-y; }

  .band { position: absolute; left: 0; top: 40px; width: 100%; background: var(--navy); }
  .screen--quote .band { height: 157px; }
  .screen--item .band { height: 156px; }

  .band__title { position: absolute; left: 49px; top: 26px; color: var(--white); font-size: 14px; font-weight: 500; }
  .band__title span { margin: 0 7px; }

  .select { position: absolute; left: 565px; top: 24px; width: 166px; height: 27px; background: var(--navy-field); color: var(--white); font-size: 9.5px; display: flex; align-items: center; }
  .select__value { flex: 1; text-align: right; padding-right: 12px; }
  .select__arrows { width: 27px; height: 100%; border-left: 1px solid rgba(255,255,255,.35); display: flex; align-items: center; justify-content: center; }

  .toggle-label { position: absolute; color: var(--white); font-size: 9.5px; font-weight: 500; }
  .toggle { position: absolute; width: 37px; height: 20px; }
  .toggle::before { content: ""; position: absolute; left: 0; right: 10px; top: 9.5px; border-top: 1.5px solid var(--white); }
  .toggle::after { content: ""; position: absolute; right: 0; top: 0; width: 20px; height: 20px; border-radius: 50%; background: var(--white); }

  .search { position: absolute; left: 29px; top: 65px; width: 827px; height: 27px; background: var(--navy-search); color: var(--white); font-size: 9.5px; font-weight: 500; display: flex; align-items: center; }
  .search__text { flex: 1; padding-left: 21px; }
  .search__btn { width: 59px; height: 100%; border-left: 1px solid rgba(255,255,255,.25); display: flex; align-items: center; justify-content: center; }

  .card { position: absolute; left: 28px; background: var(--white); box-shadow: 0 1px 3px rgba(0,0,0,.18); }
  .screen--quote .card { top: 152px; width: 830px; height: 389px; }
  .screen--item .card { top: 104px; width: 830px; height: 430px; }

  .table__row { display: grid; grid-template-columns: 28px 51px 99px 100px 125px 149px 72px 90px 55px 1fr; align-items: center; height: 33.8px; font-size: 9.6px; color: #333; }
  .table__row:nth-child(odd) { background: var(--row-alt); }
  .table__head { height: 44px; font-weight: 500; font-size: 9.4px; color: #111; border-bottom: 1px solid var(--line); display: grid; grid-template-columns: 28px 51px 99px 100px 125px 149px 72px 90px 55px 1fr; align-items: center; }
  .table__sort { color: var(--gold); position: relative; height: 100%; display: flex; align-items: center; }
  .table__sort::after { content: ""; position: absolute; left: 0; width: 83px; bottom: -1px; border-bottom: 2px solid var(--gold); }
  .table__center { text-align: center; }
  .table__trash { display: flex; justify-content: center; }

  .pager { position: absolute; left: 0; top: 361px; width: 100%; height: 12px; font-size: 8px; color: #555; }
  .pager > * { position: absolute; top: 0; display: flex; align-items: center; height: 12px; }
  .pager__label { left: 29px; }
  .pager__size { left: 110px; gap: 5px; }
  .pager__range { left: 153px; }
  .pager__prev { left: 212px; }
  .pager__next { left: 246px; }

  .back { position: absolute; left: 37px; top: 34px; display: flex; align-items: center; color: var(--white); font-size: 14.5px; font-weight: 500; }
  .back span.sep { margin: 0 14px 0 16px; }

  .gallery__frame { position: absolute; left: 10px; top: 11px; width: 263px; height: 262px; border: 1px solid var(--gold); }
  .gallery__photo { position: absolute; inset: 16px 40px; background: radial-gradient(ellipse at 50% 45%, #fafafa, #e4e4e4 70%, #fff 100%); border-radius: 6px; }
  .gallery__zoom { position: absolute; right: 6px; top: 5px; width: 21px; height: 20px; background: var(--gold); display: flex; align-items: center; justify-content: center; }
  .gallery__nav { position: absolute; left: 10px; top: 293px; width: 263px; display: flex; align-items: center; justify-content: space-between; padding: 0 34px 0 38px; font-size: 12.5px; color: #444; }
  .gallery__thumbs { position: absolute; left: 10px; top: 335px; display: flex; gap: 12px; }
  .gallery__thumb { width: 57px; height: 57px; border: 1px solid #cfcfcf; padding: 6px 12px; }
  .gallery__thumb div { width: 100%; height: 100%; background: linear-gradient(#f4f4f4, #dcdcdc); border-radius: 4px; }

  .section-title { position: absolute; left: 328px; color: var(--gold); font-size: 12px; font-weight: 500; letter-spacing: .2px; }
  .info { position: absolute; left: 328px; top: 56px; }
  .info__row { display: grid; grid-template-columns: 125px 24px auto; height: 27.7px; align-items: center; }
  .info__label { font-size: 10.8px; color: #555; }
  .info__colon { font-size: 10.8px; color: #555; }
  .info__value { font-size: 12px; font-weight: 500; color: #111; }

  .cost { position: absolute; left: 328px; top: 320px; }
  .cost__row { display: grid; grid-template-columns: 74px 86px 88px 86px 88px auto; height: 27.5px; align-items: center; font-size: 10.8px; color: #555; }
</style>
</head>
<body>

<section class="screen screen--quote">
  <header class="appbar">
    <div class="appbar__menu"></div>
    <div class="appbar__brand">LOGOHERE</div>
    <div class="appbar__user">Hi !, Admin Name</div>
    <div class="appbar__avatar" role="img" aria-label="User profile photo"></div>
    <div class="appbar__more"></div>
  </header>
  <div class="band">
    <div class="band__title">Staff View<span>|</span>Quote #1234</div>
    <div class="select">
      <div class="select__value">Dana Whitlow</div>
      <div class="select__arrows">
        <svg width="8" height="11" viewBox="0 0 8 11"><path d="M1 4 L4 1 L7 4 M1 7 L4 10 L7 7" fill="none" stroke="#fff" stroke-width="1.3"/></svg>
      </div>
    </div>
    <div class="toggle-label" style="left:765px;top:33px;">Staff</div>
    <div class="toggle" style="left:801px;top:27px;"></div>
    <div class="search">
      <div class="search__text">Search by WFS#, product code, manufacturer code or description to find a product</div>
      <div class="search__btn">
        <svg width="10" height="10" viewBox="0 0 10 10"><circle cx="4" cy="4" r="3" fill="none" stroke="#fff" stroke-width="1.6"/><path d="M6.2 6.2 L9 9" stroke="#fff" stroke-width="1.8"/></svg>
      </div>
    </div>
  </div>

  <div class="card">
    <div class="table__head">
      <span></span><span>QTY</span>
      <span class="table__sort"><svg width="9" height="9" viewBox="0 0 9 9" style="margin:0 7px 0 3px"><path d="M4.5 8 V1.5 M1.5 4.5 L4.5 1.5 L7.5 4.5" fill="none" stroke="#b38f4f" stroke-width="1"/></svg>WFS</span>
      <span>Product Code</span><span>Manufacturer Code</span><span>Description</span><span>Cost</span><span>Upgrade Cost</span><span>View</span><span class="table__center">Remove</span>
    </div>
    <div class="table__body">
      <div class="table__row"><span></span><span>1</span><span>83MB106-82</span><span>008168961A</span><span>106010500</span><span>Corvin Non-Insulated Tank</span><span>$123.00</span><span>$25.00</span><span>View</span><span class="table__trash"><svg width="11" height="13" viewBox="0 0 11 13"><rect x="0" y="1.5" width="11" height="1.8" fill="#b38f4f"/><rect x="3.5" y="0" width="4" height="1.8" fill="#b38f4f"/><path d="M1.2 4 H9.8 L9 13 H2 Z" fill="#b38f4f"/></svg></span></div>
      <div class="table__row"><span></span><span>1</span><span>83MB106-82</span><span>008168961A</span><span>106010500</span><span>Corvin Non-Insulated Tank</span><span>$123.00</span><span>$ -</span><span>View</span><span class="table__trash"><svg width="11" height="13" viewBox="0 0 11 13"><rect x="0" y="1.5" width="11" height="1.8" fill="#b38f4f"/><rect x="3.5" y="0" width="4" height="1.8" fill="#b38f4f"/><path d="M1.2 4 H9.8 L9 13 H2 Z" fill="#b38f4f"/></svg></span></div>
      <div class="table__row"><span></span><span>1</span><span>83MB106-82</span><span>008168961A</span><span>106010500</span><span>Corvin Non-Insulated Tank</span><span>$123.00</span><span>$25.00</span><span>View</span><span class="table__trash"><svg width="11" height="13" viewBox="0 0 11 13"><rect x="0" y="1.5" width="11" height="1.8" fill="#b38f4f"/><rect x="3.5" y="0" width="4" height="1.8" fill="#b38f4f"/><path d="M1.2 4 H9.8 L9 13 H2 Z" fill="#b38f4f"/></svg></span></div>
      <div class="table__row"><span></span><span>1</span><span>83MB106-82</span><span>008168961A</span><span>106010500</span><span>Corvin Non-Insulated Tank</span><span>$123.00</span><span>$ -</span><span>View</span><span class="table__trash"><svg width="11" height="13" viewBox="0 0 11 13"><rect x="0" y="1.5" width="11" height="1.8" fill="#b38f4f"/><rect x="3.5" y="0" width="4" height="1.8" fill="#b38f4f"/><path d="M1.2 4 H9.8 L9 13 H2 Z" fill="#b38f4f"/></svg></span></div>
      <div class="table__row"><span></span><span>1</span><span>83MB106-82</span><span>008168961A</span><span>106010500</span><span>Corvin Non-Insulated Tank</span><span>$123.00</span><span>$ -</span><span>View</span><span class="table__trash"><svg width="11" height="13" viewBox="0 0 11 13"><rect x="0" y="1.5" width="11" height="1.8" fill="#b38f4f"/><rect x="3.5" y="0" width="4" height="1.8" fill="#b38f4f"/><path d="M1.2 4 H9.8 L9 13 H2 Z" fill="#b38f4f"/></svg></span></div>
      <div class="table__row"><span></span><span>1</span><span>83MB106-82</span><span>008168961A</span><span>106010500</span><span>Corvin Non-Insulated Tank</span><span>$123.00</span><span>$25.00</span><span>View</span><span class="table__trash"><svg width="11" height="13" viewBox="0 0 11 13"><rect x="0" y="1.5" width="11" height="1.8" fill="#b38f4f"/><rect x="3.5" y="0" width="4" height="1.8" fill="#b38f4f"/><path d="M1.2 4 H9.8 L9 13 H2 Z" fill="#b38f4f"/></svg></span></div>
      <div class="table__row"><span></span><span>1</span><span>83MB106-82</span><span>008168961A</span><span>106010500</span><span>Corvin Non-Insulated Tank</span><span>$123.00</span><span>$ -</span><span>View</span><span class="table__trash"><svg width="11" height="13" viewBox="0 0 11 13"><rect x="0" y="1.5" width="11" height="1.8" fill="#b38f4f"/><rect x="3.5" y="0" width="4" height="1.8" fill="#b38f4f"/><path d="M1.2 4 H9.8 L9 13 H2 Z" fill="#b38f4f"/></svg></span></div>
      <div class="table__row"><span></span><span>1</span><span>83MB106-82</span><span>008168961A</span><span>106010500</span><span>Corvin Non-Insulated Tank</span><span>$123.00</span><span>$25.00</span><span>View</span><span class="table__trash"><svg width="11" height="13" viewBox="0 0 11 13"><rect x="0" y="1.5" width="11" height="1.8" fill="#b38f4f"/><rect x="3.5" y="0" width="4" height="1.8" fill="#b38f4f"/><path d="M1.2 4 H9.8 L9 13 H2 Z" fill="#b38f4f"/></svg></span></div>
      <div class="table__row"><span></span><span>1</span><span>83MB106-82</span><span>008168961A</span><span>106010500</span><span>Corvin Non-Insulated Tank</span><span>$123.00</span><span>$25.00</span><span>View</span><span class="table__trash"><svg width="11" height="13" viewBox="0 0 11 13"><rect x="0" y="1.5" width="11" height="1.8" fill="#b38f4f"/><rect x="3.5" y="0" width="4" height="1.8" fill="#b38f4f"/><path d="M1.2 4 H9.8 L9 13 H2 Z" fill="#b38f4f"/></svg></span></div>
    </div>
    <div class="pager">
      <span class="pager__label">Rows per page:</span>
      <span class="pager__size">7 <svg width="9" height="5" viewBox="0 0 9 5"><path d="M0 0 H9 L4.5 5 Z" fill="#b38f4f"/></svg></span>
      <span class="pager__range">1-7 of 13</span>
      <span class="pager__prev"><svg width="5" height="8" viewBox="0 0 5 8"><path d="M4 1 L1 4 L4 7" fill="none" stroke="#ccc" stroke-width="1.2"/></svg></span>
      <span class="pager__next"><svg width="5" height="8" viewBox="0 0 5 8"><path d="M1 1 L4 4 L1 7" fill="none" stroke="#b38f4f" stroke-width="1.4"/></svg></span>
    </div>
  </div>
</section>

<section class="screen screen--item">
  <header class="appbar">
    <div class="appbar__menu"></div>
    <div class="appbar__brand">LOGOHERE</div>
    <div class="appbar__user">Hi !, Admin Name</div>
    <div class="appbar__avatar" role="img" aria-label="User profile photo"></div>
    <div class="appbar__more"></div>
  </header>
  <div class="band">
    <div class="back">
      <svg width="11" height="18" viewBox="0 0 11 18" style="margin-right:14px"><path d="M9 1.5 L2 9 L9 16.5" fill="none" stroke="#fff" stroke-width="2"/></svg>
      Back<span class="sep">|</span>Item 83MB196-82
    </div>
    <div class="toggle-label" style="left:729px;top:39px;">Product Cost</div>
    <div class="toggle" style="left:801px;top:34px;"></div>
  </div>

  <div class="card">
    <div class="gallery__frame">
      <div class="gallery__photo" role="img" aria-label="Product photo of a white two-piece round-front toilet"></div>
      <div class="gallery__zoom">
        <svg width="13" height="13" viewBox="0 0 13 13"><circle cx="5.5" cy="5.5" r="4" fill="none" stroke="#fff" stroke-width="1.6"/><path d="M8.5 8.5 L12 12" stroke="#fff" stroke-width="2"/><path d="M3.5 5.5 H7.5 M5.5 3.5 V7.5" stroke="#fff" stroke-width="1.2"/></svg>
      </div>
    </div>
    <div class="gallery__nav">
      <svg width="9" height="16" viewBox="0 0 9 16"><path d="M8 1 L1 8 L8 15" fill="none" stroke="#bbb" stroke-width="1.4"/></svg>
      <span>Picture 1 Of 5</span>
      <svg width="9" height="16" viewBox="0 0 9 16"><path d="M1 1 L8 8 L1 15" fill="none" stroke="#b38f4f" stroke-width="1.8"/></svg>
    </div>
    <div class="gallery__thumbs">
      <div class="gallery__thumb" role="img" aria-label="Product thumbnail 1"><div></div></div>
      <div class="gallery__thumb" role="img" aria-label="Product thumbnail 2"><div></div></div>
      <div class="gallery__thumb" role="img" aria-label="Product thumbnail 3"><div></div></div>
      <div class="gallery__thumb" role="img" aria-label="Product thumbnail 4"><div></div></div>
    </div>

    <div class="section-title" style="top:22px;">MAIN INFORMATION</div>
    <div class="info">
      <div class="info__row"><span class="info__label">WFS#</span><span class="info__colon">:</span><span class="info__value">83MB196-82</span></div>
      <div class="info__row"><span class="info__label">WFS Descripriton</span><span class="info__colon">:</span><span class="info__value">VELA ROUND FRONT 12’ ROUGH IN</span></div>
      <div class="info__row"><span class="info__label">Vendor Descriptions</span><span class="info__colon">:</span><span class="info__value">VELA BOWL 130 ROUND WHITE</span></div>
      <div class="info__row"><span class="info__label">MFG</span><span class="info__colon">:</span><span class="info__value">Harbrook</span></div>
      <div class="info__row"><span class="info__label">Part #</span><span class="info__colon">:</span><span class="info__value">130010007</span></div>
      <div class="info__row"><span class="info__label">MFG #</span><span class="info__colon">:</span><span class="info__value">130010007</span></div>
      <div class="info__row"><span class="info__label">Vendor Code</span><span class="info__colon">:</span><span class="info__value">130</span></div>
      <div class="info__row"><span class="info__label">Cost</span><span class="info__colon">:</span><span class="info__value">$ 123.00</span></div>
    </div>

    <div class="section-title" style="top:292px;">PRODUCT COST</div>
    <div class="cost">
      <div class="cost__row"><span>List Price</span><span>: $150.00</span><span>Vendor Price</span><span>: $149.00</span><span>Vendor Price</span><span>: $ 150.00</span></div>
      <div class="cost__row"><span>List Price</span><span>: $150.00</span><span>Vendor Price</span><span>: $149.00</span><span>Vendor Price</span><span>: $ 150.00</span></div>
      <div class="cost__row"><span>List Price</span><span>: $150.00</span><span>Vendor Price</span><span>: $149.00</span><span>Vendor Price</span><span>: $ 150.00</span></div>
    </div>
  </div>
</section>

</body>
</html>
```